Business Card Design Project

I need a new business card design for my building/development company: Ridgewell Constructions.

We specialise in small sub-divisions, multi-story developments and new house builds.
We handle the whole process from concept stage right throught to a fully developed property.
Updates

Project Deadline Extended
Reason: Need a couple of extra days to decide as there are so many amazing designs

Target Market(s)

people looking to develop their property and need help. New property buyers

Industry/Entity Type

House

Requirements
Must have
• My logo on both sides:
Side 1: Logo taking up whole side as per old card but with a color/style change.

Side 2: Contact page: include logo but the rest just surprise me!

All contact details will be: (and need to be changable for each employee) I'll inform you of specifics before printing.

Name Surname
Position ie. Managing director
M: insert mobile
E: insert email
P.O. Box 518, Elmhurst, Vic, 3145
www.ridgewellconstructions.com.au

Nice to have
• Colors i'd like: (not necessarily all but this is the basic idea)

Black, blue, grey, silver, white

```html
<!DOCTYPE html>
<html lang="en">
<head>
<meta charset="utf-8">
<title>Ridgewell Constructions – Business Cards</title>
<link rel="stylesheet" href="https://fonts.googleapis.com/css2?family=Source+Sans+3:wght@400;600;700&display=swap">
<style>
  :root {
    --backdrop: #a8822a;
    --card: #ffffff;
    --brand-blue: #1a8fd6;
    --band-light: #a9d8f2;
    --ink: #1b1b1b;
    --text: #2a2a2a;
    --band-dark: #0c0c0c;
  }
  * { box-sizing: border-box; margin: 0; padding: 0; }
  html, body { width: 1200px; height: 686px; overflow: hidden; }
  body {
    background: var(--backdrop);
    font-family: "Source Sans 3", sans-serif;
    color: var(--text);
    position: relative;
  }
  .card {
    position: absolute;
    width: 510px;
    height: 291px;
    background: var(--card);
    border-radius: 14px;
    overflow: hidden;
    box-shadow: 1px 2px 3px rgba(0,0,0,0.35);
  }
  .card--contact-inline { left: 67px; top: 30px; }
  .card--contact-columns { left: 67px; top: 352px; }
  .card--logo-side { left: 621px; top: 303px; }

  .brand {
    position: absolute;
    left: 0; right: 0;
    text-align: center;
    line-height: 1;
  }
  .brand__name {
    display: inline-flex;
    align-items: center;
    gap: 8px;
    color: var(--brand-blue);
    font-weight: 600;
    font-size: 27px;
  }
  .brand__mark {
    width: 16px; height: 16px;
    background: var(--brand-blue);
  }
  .brand__tagline {
    display: block;
    margin-top: 4px;
    color: var(--ink);
    font-size: 11.5px;
    font-weight: 600;
    letter-spacing: 0.2px;
  }
  .card--contact-inline .brand { top: 107px; }
  .card--contact-columns .brand { top: 106px; }
  .card--logo-side .brand { top: 153px; }
  .card--logo-side .brand__name { font-size: 34px; }
  .card--logo-side .brand__mark { width: 20px; height: 20px; }
  .card--logo-side .brand__tagline { font-size: 14.5px; margin-top: 5px; }

  .label { color: var(--brand-blue); font-weight: 700; }
  .person-name { color: var(--brand-blue); font-weight: 700; font-size: 15.5px; }
  .person-role { color: var(--ink); font-weight: 700; font-size: 12px; }

  .contact-inline {
    position: absolute;
    left: 0; right: 0; top: 172px;
    text-align: center;
    font-size: 12px;
    line-height: 17px;
  }
  .contact-inline__title { margin-bottom: 3px; }
  .contact-inline__title .divider {
    display: inline-block;
    width: 1px; height: 15px;
    background: var(--ink);
    margin: 0 4px;
    vertical-align: -2px;
  }
  .gap { display: inline-block; width: 16px; }

  .contact-columns {
    position: absolute;
    top: 168px;
    font-size: 12px;
    line-height: 17px;
  }
  .contact-columns__identity {
    position: absolute;
    right: 318px;
    text-align: right;
    white-space: nowrap;
  }
  .contact-columns__identity .person-name { line-height: 19px; }
  .contact-columns__rule {
    position: absolute;
    left: 206px; top: 178px;
    width: 1px; height: 60px;
    background: var(--ink);
  }
  .contact-columns__details {
    position: absolute;
    left: 221px;
    white-space: nowrap;
  }

  .band {
    position: absolute;
    left: 0; bottom: 0;
    width: 510px; height: 30px;
  }
  .band__url {
    position: absolute;
    right: 16px; bottom: 7px;
    color: #fff;
    font-weight: 700;
    font-size: 12.5px;
  }
</style>
</head>
<body>

  <svg width="0" height="0" style="position:absolute" aria-hidden="true">
    <defs>
      <linearGradient id="bandGradient" x1="0" y1="0" x2="1" y2="0">
        <stop offset="0" stop-color="#a9d8f2"/>
        <stop offset="0.55" stop-color="#1a8fd6"/>
        <stop offset="1" stop-color="#1a8fd6"/>
      </linearGradient>
    </defs>
  </svg>

  <!-- Contact side, single centred block -->
  <section class="card card--contact-inline">
    <div class="brand">
      <span class="brand__name"><span class="brand__mark"></span>Ridgewell Constructions</span>
      <span class="brand__tagline">renovation-construction-development</span>
    </div>
    <div class="contact-inline">
      <p class="contact-inline__title"><span class="person-name">Martin Calloway</span><span class="divider"></span><span class="person-role">Managing director</span></p>
      <p><span class="label">Ph/Fax</span> : 03 9460 2815<span class="gap"></span><span class="label">Mob</span> : 0400 555 217</p>
      <p><span class="label">ABN</span> : 51 824 670 392<span class="gap"></span><span class="label">Email</span> : ridgewell@mailhub.com.au</p>
      <p>P.O. Box 518, Elmhurst, Vic, 3145</p>
    </div>
    <svg class="band" viewBox="0 0 510 30" aria-hidden="true">
      <rect x="0" y="13" width="290" height="17" fill="var(--band-dark)"/>
      <polygon points="289,0 510,0 510,30 277,30" fill="url(#bandGradient)"/>
    </svg>
    <span class="band__url">www.ridgewellconstructions.com.au</span>
  </section>

  <!-- Contact side, two columns -->
  <section class="card card--contact-columns">
    <div class="brand">
      <span class="brand__name"><span class="brand__mark"></span>Ridgewell Constructions</span>
      <span class="brand__tagline">renovation-construction-development</span>
    </div>
    <div class="contact-columns" style="left:0; right:0;">
      <div class="contact-columns__identity">
        <p class="person-name">Martin Calloway</p>
        <p class="person-role">Managing director</p>
        <p style="margin-top:4px">P.O. Box 518</p>
        <p>Elmhurst, Vic, 3145</p>
      </div>
      <div class="contact-columns__details">
        <p><span class="label">Ph/Fax</span> : 03 9460 2815</p>
        <p><span class="label">Mob</span> : 0400 555 217</p>
        <p><span class="label">ABN</span> : 51 824 670 392</p>
        <p><span class="label">Email</span> : ridgewell@mailhub.com.au</p>
      </div>
    </div>
    <div class="contact-columns__rule"></div>
    <svg class="band" viewBox="0 0 510 30" aria-hidden="true">
      <rect x="0" y="13" width="290" height="17" fill="var(--band-dark)"/>
      <polygon points="289,0 510,0 510,30 277,30" fill="url(#bandGradient)"/>
    </svg>
    <span class="band__url">www.ridgewellconstructions.com.au</span>
  </section>

  <!-- Logo side -->
  <section class="card card--logo-side">
    <div class="brand">
      <span class="brand__name"><span class="brand__mark"></span>Ridgewell Constructions</span>
      <span class="brand__tagline">renovation-construction-development</span>
    </div>
    <svg class="band" viewBox="0 0 510 30" aria-hidden="true">
      <rect x="0" y="13" width="290" height="17" fill="var(--band-dark)"/>
      <polygon points="289,0 510,0 510,30 277,30" fill="url(#bandGradient)"/>
    </svg>
    <span class="band__url">www.ridgewellconstructions.com.au</span>
  </section>

</body>
</html>
```